【 概要 】 都内で7年目のイタリアンレストランです。 コロナ渦でテイクアウト営業に勤しんでおります。 今までスタッフが書いたチラシで頑張ってましたが、メニュー改訂もあり是非プロのお力添えを頂きたく募集致しました。 素敵なデザインを楽しみにしております。 【 依頼内容 】 ・サイズ:A4 片面 ・ページ数:1ページ ・素材の用意(画像・文章等):添付ファイル1枚目がメニューです ・デザイン内容:添付ファイル2枚目がイメージです。料理や人物を参考にお願いします 【 デザインイメージ 】 ・ターゲット層:都心在住の30〜50代男女 ・雰囲気:ナチュラルでおしゃれな雰囲気 ・参考デザイン: お店のイメージ(URL参考)添付ファイル2枚目参照 【 契約金額(税抜) 】 2万円 ※契約金額(税込)からシステム利用料を差し引いた金額が、ワーカーさまの受取金額となります その他ご質問等ありましたら、気軽にお問い合わせください。 ご応募をお待ちしております! |
| https://find.kumoriba.co.jp/amp/s/s.shokunavi-ranpo.jp/tokyo/B2401/B240305/24085917/top_amp/%3Fusqp%3Dxr482KZTMBHZBafV9N3q9-vY6RHxBTB%253D | ||
この度は有難うございます。また細かな修正も早急に対応してくださりありがたかったです。お陰で妥協なくイメージしたデザインに仕上がりました。スキルも高く誠意も伝わりとても感謝致します。また機会がございましたら宜しくお願い致します。
この度は皆様素敵なデザインをありがとうございました!皆様の素敵なデザインに感動し感謝の気持ちでいっぱいでした。コロナ渦で皆様も大変な状況だと思いますが、私も頑張ろうという気持ちになりました。心からありがとうございました。

```html
<!DOCTYPE html>
<html lang="ja">
<head>
<meta charset="utf-8">
<title>TORATTORIA VENTO テイクアウトメニュー</title>
<link rel="stylesheet" href="https://fonts.googleapis.com/css2?family=Cormorant+Garamond:wght@600;700&family=Marcellus&family=Noto+Sans+JP:wght@400;500;700&family=Noto+Serif+JP:wght@500&display=swap">
<style>
  :root {
    --marble: #efe1d6;
    --marble-deep: #e3cfc1;
    --ink: #3a2f2a;
    --green: #2f7d3a;
    --red: #c8322b;
    --white: #fbf7f2;
  }
  * { box-sizing: border-box; margin: 0; padding: 0; }
  html, body { width: 848px; height: 1200px; overflow: hidden; }
  body {
    position: relative;
    font-family: "Noto Sans JP", sans-serif;
    color: var(--ink);
    background: radial-gradient(ellipse at 30% 20%, #f6ece4 0%, var(--marble) 45%, var(--marble-deep) 100%);
  }
  .brand { position: absolute; left: 22px; top: 22px; }
  .brand-sub { font-family: "Marcellus", serif; font-size: 22px; letter-spacing: 2px; }
  .brand-name { font-family: "Cormorant Garamond", serif; font-weight: 700; font-size: 84px; line-height: .95; letter-spacing: 3px; }
  .brand-tel { font-weight: 500; font-size: 30px; color: var(--green); margin-top: 4px; letter-spacing: 1px; }
  .reserve {
    position: absolute; left: 340px; top: 112px; width: 90px; height: 46px;
    background: var(--red); color: var(--white); font-size: 11px; line-height: 1.5;
    display: flex; align-items: center; justify-content: center; text-align: center; white-space: nowrap;
  }
  .stripe { position: absolute; left: 0; width: 430px; height: 6px; }
  .stripe.green { top: 170px; background: var(--green); }
  .stripe.red { top: 180px; background: var(--red); }
  .takeout { position: absolute; left: 455px; top: 12px; width: 350px; height: 250px; }
  .takeout-art { position: absolute; left: 60px; top: 110px; width: 230px; height: 120px; background: linear-gradient(#e6d6ca, #dcc8ba); opacity: .7; }
  .takeout-title { position: absolute; left: 0; top: 62px; width: 100%; text-align: center; font-family: "Noto Serif JP", serif; font-size: 28px; letter-spacing: 3px; }
  .takeout-lead { position: absolute; right: 18px; top: 14px; font-size: 13px; transform: rotate(-28deg); }

  .section { position: absolute; }
  .section h2 {
    font-family: "Marcellus", serif; font-weight: 400; font-size: 34px; letter-spacing: 1px;
    border-bottom: 3px solid var(--green); padding-bottom: 2px; margin-bottom: 8px; line-height: 1.15;
  }
  .section h2 small { font-family: "Noto Sans JP", sans-serif; font-size: 14px; }
  .section ul { list-style: none; }
  .section li { display: flex; justify-content: space-between; gap: 8px; font-size: 16px; line-height: 24px; font-weight: 500; white-space: nowrap; }
  .section li .sub { padding-left: 5em; }
  .col-left { left: 22px; width: 378px; }
  .col-right { left: 445px; width: 385px; }
  .row-1 { top: 318px; }
  .row-2 { top: 545px; }
  .row-3 { top: 762px; }

  .hours {
    position: absolute; left: 445px; top: 880px; width: 385px; height: 76px;
    border: 1px solid var(--ink); padding: 6px 10px; font-size: 13px; line-height: 1.45;
  }
  .photos { position: absolute; left: 0; top: 985px; width: 848px; height: 215px; display: flex; }
  .photo { flex: 1; }
  .photo.clams { background: linear-gradient(135deg, #c8bca8, #8d7c64); }
  .photo.pizza { background: radial-gradient(circle at 50% 55%, #d8a25c, #b3552f 60%, #4f3a2a); }
  .photo.dolce { background: linear-gradient(135deg, #b8a890, #6a4a38); }
</style>
</head>
<body>
  <header class="brand">
    <div class="brand-sub">TORATTORIA</div>
    <div class="brand-name">VENTO</div>
    <div class="brand-tel">03-5018-2740</div>
  </header>
  <div class="reserve">前日ご予約<br>お願い致します</div>
  <div class="stripe green"></div>
  <div class="stripe red"></div>

  <div class="takeout">
    <svg width="350" height="250" viewBox="0 0 350 250">
      <polygon points="175,6 342,92 300,244 50,244 8,92" fill="none" stroke="#3a2f2a" stroke-width="2"/>
    </svg>
    <div class="takeout-lead">おうちで食べよう</div>
    <div class="takeout-title">テイクアウト</div>
    <div class="takeout-art" role="img" aria-label="持ち帰り袋を持って歩く人とスプーン・フォークのイラスト"></div>
  </div>

  <section class="section col-left row-1">
    <h2>ANTIPAST</h2>
    <ul>
      <li><span>ゴルゴンゾーラのキッシュ(2P)</span><span>¥800</span></li>
      <li><span>ピクルス&amp;オリーブ</span><span>¥500</span></li>
      <li><span>合鴨のロースト</span><span>¥900</span></li>
      <li><span>いいだこのトマト煮</span><span>¥950</span></li>
      <li><span>ローストビーフ</span><span>¥1200</span></li>
      <li><span>ローストポーク</span><span>¥900</span></li>
    </ul>
  </section>

  <section class="section col-right row-1">
    <h2>SPECIALITA</h2>
    <ul>
      <li><span>天使の海老のクリーム煮</span><span>¥700</span></li>
      <li><span>つぶ貝と小海老のエスカルゴバター</span><span>¥900</span></li>
      <li><span>魚介の旨み凝縮アヒージョ</span><span></span></li>
      <li><span class="sub">〜スープ仕立て〜</span><span>¥900</span></li>
      <li><span>ラザニア</span><span>¥900</span></li>
      <li><span>バゲット(2P)</span><span>¥300</span></li>
    </ul>
  </section>

  <section class="section col-left row-2">
    <h2>PAST <small>(麺は全てリングイネです)</small></h2>
    <ul>
      <li><span>はまぐりと大葉おろしのボンゴレビアンコ</span><span>¥1500</span></li>
      <li><span>渡り蟹のトマトクリームパスタ</span><span>¥1500</span></li>
      <li><span>にんにくとアンチョビのペペロンチーノ</span><span>¥900</span></li>
      <li><span>ゴルゴンゾーラのペンネ</span><span>¥1300</span></li>
      <li><span>アラビアータのペンネ</span><span>¥1200</span></li>
    </ul>
  </section>

  <section class="section col-right row-2">
    <h2>INSALATA <small>(3〜4名様)</small></h2>
    <ul>
      <li><span>生ハムのグリーンサラダ</span><span>¥1000</span></li>
      <li><span>イタリアンだけどフレンチサラダ</span><span>¥1000</span></li>
      <li><span class="sub">Sサイズ</span><span>¥450</span></li>
      <li><span>VENTOのシーザーサラダ</span><span>¥1000</span></li>
    </ul>
  </section>

  <section class="section col-left row-3">
    <h2>PIZZA</h2>
    <ul>
      <li><span>マルゲリータ</span><span>¥1500</span></li>
      <li><span>4種チーズのクアトロフォロマッジョ</span><span>¥1700</span></li>
      <li><span>博多明太子のクリームピザ</span><span>¥1600</span></li>
      <li><span>ザ・サルシッチャ</span><span>¥1500</span></li>
    </ul>
  </section>

  <section class="section col-right row-3">
    <h2>DOLCE</h2>
    <ul>
      <li><span>ガトーショコラ</span><span>¥500</span></li>
      <li><span>ティラミス</span><span>¥500</span></li>
    </ul>
  </section>

  <div class="hours">
    ランチ　　11:00〜15:00(土日祝11:30〜15:00)<br>
    ディナー　17:00〜23:00<br>
    テイクアウト16:30〜21:00(土日祝はランチからOK)
  </div>

  <div class="photos">
    <div class="photo clams" role="img" aria-label="あさりのパスタの写真"></div>
    <div class="photo pizza" role="img" aria-label="マルゲリータピザの写真"></div>
    <div class="photo dolce" role="img" aria-label="ティラミスとベリーのデザートの写真"></div>
  </div>
</body>
</html>
```